Kestrel Building Works Business Card and more!

We need a business card design for Kestrel Building Works Ltd, a respected building company that specialises in high quality designer homes.

We're after a sleek, clean, modern business card that incorporates our new logo (see attached) and colours, with black being the background.

We are Certified Framing Guild and need to include their logo (see attached) on our cards, balancing but not taking over our logo.

Details to be included:

Malcolm Tivey
Director

Phone: 0218845126
Email: kestrelbuild.nz@maildrop-example.co.nz
Website: www.kestrelbuildingworks-example.co.nz

Additional Information

A start up website is also under construction and needing attention and letterheads are needed!

We look forward to your designs!

Target Market(s)

30+ people who are interested in building new or renovating current homes

Industry/Entity Type

Construction

Contact Information for Business Card

Malcolm Tivey
Director

Phone: 0218845126
Facebook: www.socialpage-example.com/kestrelbuild.nz

Font styles to use
Serif

Colors

Designer to choose colors to be used in the design.

Requirements
Must have
• Our new logo
• Our colours
• cfg logo

```html
<!DOCTYPE html>
<html lang="en">
<head>
<meta charset="utf-8">
<title>Kestrel Building Works – Business Card</title>
<link rel="stylesheet" href="https://fonts.googleapis.com/css2?family=Roboto+Condensed:wght@400;700&family=Roboto:wght@400&display=swap">
<style>
  :root {
    --bg: #d9d6d1;
    --card-dark: #111213;
    --card-mid: #2a2b2d;
    --gold: #c9965a;
    --white: #f4f1ec;
    --grey: #cfcac3;
  }
  * { box-sizing: border-box; margin: 0; padding: 0; }
  html, body { width: 1200px; height: 1200px; overflow: hidden; }
  body {
    background: var(--bg);
    font-family: "Roboto Condensed", Arial, sans-serif;
    position: relative;
  }
  .card {
    position: absolute;
    left: 190px;
    width: 820px;
    height: 470px;
    background: radial-gradient(ellipse at 35% 45%, var(--card-mid) 0%, var(--card-dark) 75%);
    box-shadow: 0 10px 30px rgba(0,0,0,0.25);
    color: var(--white);
    overflow: hidden;
  }
  .card--front { top: 90px; }
  .card--back { top: 640px; }

  /* Front */
  .front-brand {
    position: absolute;
    top: 170px; left: 0; right: 0;
    display: flex; align-items: center; justify-content: center; gap: 16px;
  }
  .brand-dot {
    width: 18px; height: 18px; border-radius: 50%;
    background: var(--gold);
  }
  .brand-name {
    font-family: "Roboto Condensed", Arial, sans-serif;
    font-weight: 400;
    font-size: 46px;
    letter-spacing: 6px;
    text-transform: uppercase;
    color: var(--white);
  }
  .front-social {
    position: absolute;
    top: 270px; left: 0; right: 0;
    text-align: center;
    font-family: "Roboto", Arial, sans-serif;
    font-size: 24px;
    letter-spacing: 1px;
    color: var(--gold);
  }

  /* Back */
  .guide { position: absolute; background: var(--gold); }
  .guide--vertical { left: 400px; top: 40px; width: 1.5px; height: 290px; }
  .guide--horizontal { left: 60px; top: 190px; width: 710px; height: 1.5px; }
  .guide-dot { position: absolute; width: 8px; height: 8px; border-radius: 50%; background: var(--gold); }

  .back-brand {
    position: absolute; left: 60px; top: 100px; width: 320px;
    display: flex; align-items: center; justify-content: center; gap: 10px;
  }
  .back-brand .brand-name { font-size: 24px; letter-spacing: 3px; }
  .back-brand .brand-dot { width: 11px; height: 11px; }

  .guild-badge {
    position: absolute; left: 170px; top: 215px;
    width: 104px; height: 104px; border-radius: 50%;
    background: var(--white);
  }

  .person { position: absolute; left: 430px; top: 118px; }
  .person-name { font-weight: 700; font-size: 38px; letter-spacing: 1px; text-transform: uppercase; line-height: 1; }
  .person-role { font-size: 16px; color: var(--grey); margin-top: 8px; }

  .contacts { position: absolute; left: 430px; top: 210px; list-style: none; }
  .contacts li { display: flex; align-items: center; gap: 12px; font-size: 18px; height: 28px; color: var(--white); }
  .contact-icon {
    width: 20px; height: 20px; border-radius: 4px; background: var(--gold);
    display: flex; align-items: center; justify-content: center; flex: none;
  }

  .back-website {
    position: absolute; left: 60px; right: 60px; top: 375px;
    font-family: "Roboto", Arial, sans-serif;
    font-size: 26px; letter-spacing: 4.5px;
    color: var(--gold);
    text-align: center;
  }
</style>
</head>
<body>

<section class="card card--front">
  <div class="front-brand">
    <span class="brand-dot"></span>
    <span class="brand-name">Kestrel Building Works</span>
  </div>
  <p class="front-social">www.socialpage-example.com/kestrelbuild.nz</p>
</section>

<section class="card card--back">
  <div class="guide guide--vertical"></div>
  <div class="guide guide--horizontal"></div>
  <span class="guide-dot" style="left:396px; top:36px;"></span>
  <span class="guide-dot" style="left:396px; top:326px;"></span>
  <span class="guide-dot" style="left:56px; top:186px;"></span>
  <span class="guide-dot" style="left:766px; top:186px;"></span>

  <div class="back-brand">
    <span class="brand-dot"></span>
    <span class="brand-name">Kestrel Building Works</span>
  </div>

  <div class="guild-badge" role="img" aria-label="Certified Framing Guild badge"></div>

  <div class="person">
    <h1 class="person-name">Malcolm Tivey</h1>
    <p class="person-role">Director</p>
  </div>

  <ul class="contacts">
    <li>
      <span class="contact-icon">
        <svg width="12" height="12" viewBox="0 0 12 12"><path d="M2.5 1h2l1 2.5-1.3 1a6 6 0 0 0 3.3 3.3l1-1.3L11 7.5v2a1 1 0 0 1-1 1A9 9 0 0 1 1.5 2a1 1 0 0 1 1-1z" fill="#111213"/></svg>
      </span>
      0218845126
    </li>
    <li>
      <span class="contact-icon">
        <svg width="12" height="10" viewBox="0 0 12 10"><rect x="0.5" y="0.5" width="11" height="9" rx="1" fill="#111213"/><path d="M1 1l5 4 5-4" stroke="#c9965a" stroke-width="1" fill="none"/></svg>
      </span>
      kestrelbuild.nz@maildrop-example.co.nz
    </li>
    <li>
      <span class="contact-icon" role="img" aria-label="Social page"></span>
      /kestrelbuild.nz
    </li>
    <li>
      <span class="contact-icon">
        <svg width="12" height="12" viewBox="0 0 12 12"><circle cx="6" cy="6" r="5" stroke="#111213" stroke-width="1.2" fill="none"/><ellipse cx="6" cy="6" rx="2" ry="5" stroke="#111213" stroke-width="1" fill="none"/><path d="M1 6h10" stroke="#111213" stroke-width="1"/></svg>
      </span>
      www.kestrelbuildingworks-example.co.nz
    </li>
  </ul>

  <p class="back-website">www.kestrelbuildingworks-example.co.nz</p>
</section>

</body>
</html>
```